orbit wellness loft
Project: logo for fitness studio
logo for fitness studio - Health
logo for fitness studio
Simple
Laura Whitfield
Certified Personal Trainer
482 W. Timber Ridge Rd. ElReno Ok. 73021
orbitwellness.owl@examplemail.test
I have already sent you most of my information .If you need more let me know .
Donna01 Donna01
I can't figure out how to change my brief. The email is wrong it's .owl@examplemail.test not .wol@examplemail.test so sorry. Also not so sure I like the black. The feeling I'm after is beach, sun and sand etc. thanks

```html
<!DOCTYPE html>
<html lang="en">
<head>
<meta charset="utf-8">
<title>orbit wellness loft – business card</title>
<link rel="stylesheet" href="https://fonts.googleapis.com/css2?family=Open+Sans:wght@300;400;600;700&display=swap">
<style>
  :root {
    --page-bg: #e9eaec;
    --card-bg: #ffffff;
    --aqua: #5fe0e4;
    --aqua-dark: #2fc4cc;
    --accent-line: #a3163c;
    --ink: #2f3336;
    --ink-soft: #4a4f53;
  }
  * { box-sizing: border-box; margin: 0; padding: 0; }
  html, body {
    width: 1200px; height: 816px; overflow: hidden;
    background: var(--page-bg);
    font-family: "Open Sans", Arial, sans-serif;
    color: var(--ink);
  }
  .card {
    position: absolute; left: 120px; top: 134px;
    width: 960px; height: 548px;
    background: var(--card-bg);
    border-radius: 44px;
    box-shadow: 0 10px 30px rgba(0,0,0,0.12);
    overflow: hidden;
  }
  .brand {
    position: absolute; left: 46px; top: 92px;
    display: flex; align-items: center; gap: 20px;
  }
  .brand-dot {
    width: 64px; height: 64px; border-radius: 50%;
    background: var(--aqua);
    flex: none;
  }
  .brand-name {
    font-weight: 300; color: var(--aqua-dark);
    font-size: 44px; line-height: 1.05; letter-spacing: 1px;
  }
  .accent-rule {
    position: absolute; left: 400px; right: 0; top: 196px;
    height: 3px; background: var(--accent-line);
  }
  .name-band {
    position: absolute; left: 0; top: 236px;
    width: 440px; height: 86px;
    background: var(--aqua);
    border-radius: 0 43px 43px 0;
    padding: 12px 0 0 56px;
  }
  .person-name { font-size: 30px; font-weight: 600; color: var(--ink); line-height: 1.15; }
  .person-title { font-size: 15px; font-weight: 700; letter-spacing: 1.2px; color: var(--ink); margin-top: 2px; }
  .contact-list {
    position: absolute; left: 52px; top: 372px;
    list-style: none;
  }
  .contact-list li {
    display: flex; align-items: center; gap: 16px;
    font-size: 19px; color: var(--ink-soft); height: 40px;
  }
  .icon { width: 20px; height: 20px; fill: var(--aqua-dark); flex: none; }
  .address {
    position: absolute; left: 600px; top: 250px;
    display: flex; gap: 14px;
    font-size: 19px; color: var(--ink-soft); line-height: 1.4;
  }
  .address .icon { margin-top: 4px; }
</style>
</head>
<body>
  <main class="card">
    <div class="brand">
      <div class="brand-dot"></div>
      <div class="brand-name">orbit wellness<br>loft</div>
    </div>
    <div class="accent-rule"></div>

    <div class="name-band">
      <p class="person-name">Laura Whitfield</p>
      <p class="person-title">CERTIFIED PERSONAL TRAINER</p>
    </div>

    <ul class="contact-list">
      <li>
        <svg class="icon" viewBox="0 0 24 24" aria-hidden="true"><path d="M6.6 10.8a15.1 15.1 0 0 0 6.6 6.6l2.2-2.2c.3-.3.7-.4 1-.2 1.1.4 2.3.6 3.6.6.6 0 1 .4 1 1V20c0 .6-.4 1-1 1A17 17 0 0 1 3 4c0-.6.4-1 1-1h3.5c.6 0 1 .4 1 1 0 1.3.2 2.5.6 3.6.1.3 0 .7-.2 1z"/></svg>
        +2 (0100) 45-616-70
      </li>
      <li>
        <svg class="icon" viewBox="0 0 24 24" aria-hidden="true"><path d="M3 5h18v14H3z M3 5l9 7 9-7" stroke="#fff" stroke-width="1.6"/></svg>
        orbitwellness.owl@examplemail.test
      </li>
      <li>
        <svg class="icon" viewBox="0 0 24 24" aria-hidden="true"><circle cx="12" cy="12" r="10"/><path d="M2 12h20M12 2c3 3 3 17 0 20M12 2c-3 3-3 17 0 20" stroke="#fff" stroke-width="1.4" fill="none"/></svg>
        www.orbitwellness.test
      </li>
    </ul>

    <div class="address">
      <svg class="icon" viewBox="0 0 24 24" aria-hidden="true"><path d="M12 3 2 12h3v9h5v-6h4v6h5v-9h3z"/></svg>
      <p>482 W. Timber Ridge Rd.<br>ElReno Ok. 73021</p>
    </div>
  </main>
</body>
</html>
```